Betrieb sucht Gestaltung des Firmentransporters
Zielgruppe
Wir gestalten und fertigen individuelle Grabzeichen / Grabsteine.
Aufgabenstellung
Gesucht ist eine flächige Gestaltung / Beklebung des ganzen Fahrzeuges bzw. der Bordwände.
https://karosseriewerkstatt-nord.de/tivaro-folierungsmuster
Allerdings ist unser Fahrzeug ein Umbau, der hintere Teil hat auf 3 Seiten Bordwände, siehe Fotos.
Das Fahrzeug soll insgesamt ein wenig eleganter wirken. Telefonnummer und Adresse ist nicht unbedingt gewünscht, jedenfalls nicht vorrangig. Wir legen Wert darauf, dass unser Logo geschickt eingebunden wird und dass die Gestaltung des Fahrzeuges eine Ausstrahlung bekommt. Das Fahrzeug ist haupsächlich auf Landstraßen und in der Stadt unterwegs, manchmal überregional (Autobahn).
Wichtig ist auch, dass wir mit dem Fahrzeug Friedhöfe befahren, ein gewisses Understatement ist uns wichtig.

```html
<!DOCTYPE html>
<html lang="de">
<head>
<meta charset="utf-8">
<title>Hollbach – Fahrzeugbeschriftung</title>
<link rel="stylesheet" href="https://fonts.googleapis.com/css2?family=Montserrat:wght@500;600&display=swap">
<style>
  :root {
    --canvas: #e9e7e2;
    --stage: #f3f2ee;
    --green: #2f4944;
    --gold: #c6a45c;
    --white: #ffffff;
    --door: #4b4e51;
    --rule: #d6d3cc;
  }
  * { margin: 0; padding: 0; box-sizing: border-box; }
  html, body { width: 1200px; height: 2607px; overflow: hidden; background: var(--canvas); }
  body { font-family: "Montserrat", sans-serif; position: relative; }

  .view { position: absolute; left: 0; width: 1200px; height: 869px; background: var(--stage); border-bottom: 1px solid var(--rule); }
  .view--right { top: 0; }
  .view--rear { top: 869px; }
  .view--left { top: 1738px; }

  .panel { position: absolute; overflow: hidden; }
  .panel__art { position: absolute; left: 0; top: 0; width: 100%; height: 100%; }

  .wordmark { position: absolute; display: flex; align-items: center; gap: 10px; font-weight: 600; letter-spacing: 0.12em; text-transform: uppercase; white-space: nowrap; }
  .wordmark__dot { width: 10px; height: 10px; border-radius: 50%; background: currentColor; }
  .wordmark--gold { color: var(--gold); }
  .wordmark--light { color: var(--white); }

  .contact { position: absolute; color: var(--white); font-weight: 500; }
  .contact__line { display: flex; align-items: center; gap: 8px; white-space: nowrap; }
  .contact__gap { width: 10px; }
  .contact__web { font-weight: 600; letter-spacing: 0.06em; }
  .icon { position: static; display: block; fill: var(--gold); flex: none; }

  .door { position: absolute; width: 330px; height: 330px; background: var(--door); border-radius: 8px; }
  .door .wordmark { left: 0; right: 0; top: 145px; justify-content: center; font-size: 30px; }
</style>
</head>
<body>

<section class="view view--right">
  <div class="panel" style="left:50px; top:200px; width:1100px; height:170px;">
    <svg class="panel__art" viewBox="0 0 1100 170" preserveAspectRatio="none" aria-hidden="true">
      <rect width="1100" height="170" fill="#ffffff"/>
      <path d="M0 0 H560 C660 10 730 60 800 170 H0 Z" fill="#2f4944"/>
      <path d="M560 18 C650 26 720 70 770 170" fill="none" stroke="#ffffff" stroke-width="5"/>
      <path d="M560 0 C670 8 750 60 820 170" fill="none" stroke="#c6a45c" stroke-width="6"/>
    </svg>
    <div class="contact" style="left:50px; top:45px;">
      <div class="contact__line" style="font-size:17px;">
        <svg class="icon" width="16" height="16" viewBox="0 0 24 24"><path d="M6.6 10.8a15 15 0 0 0 6.6 6.6l2.2-2.2a1 1 0 0 1 1-.25 11.4 11.4 0 0 0 3.6.57 1 1 0 0 1 1 1V20a1 1 0 0 1-1 1A17 17 0 0 1 3 4a1 1 0 0 1 1-1h3.5a1 1 0 0 1 1 1c0 1.25.2 2.45.57 3.57a1 1 0 0 1-.25 1z"/></svg>
        <span>036-5520-7391</span><span class="contact__gap"></span>
        <svg class="icon" width="14" height="16" viewBox="0 0 24 24"><path d="M12 2a7 7 0 0 0-7 7c0 5 7 13 7 13s7-8 7-13a7 7 0 0 0-7-7zm0 9.5A2.5 2.5 0 1 1 12 6.5a2.5 2.5 0 0 1 0 5z"/></svg>
        <span>Lindenweg 14 · 98560 Tannrode</span>
      </div>
      <div class="contact__line contact__web" style="font-size:32px; margin-top:14px;">www.steinmetz-hollbach.de</div>
    </div>
    <div class="wordmark wordmark--gold" style="left:850px; top:68px; font-size:28px;"><span class="wordmark__dot"></span>Hollbach</div>
  </div>
  <div class="door" style="left:435px; top:460px;">
    <div class="wordmark wordmark--light"><span class="wordmark__dot"></span>Hollbach</div>
  </div>
</section>

<section class="view view--rear">
  <div class="panel" style="left:100px; top:320px; width:1000px; height:200px; background:var(--green);">
    <div class="wordmark wordmark--light" style="left:40px; top:82px; font-size:28px;"><span class="wordmark__dot"></span>Hollbach</div>
    <div class="contact" style="left:330px; top:48px;">
      <div class="contact__line" style="font-size:21px;">
        <svg class="icon" width="20" height="20" viewBox="0 0 24 24"><path d="M6.6 10.8a15 15 0 0 0 6.6 6.6l2.2-2.2a1 1 0 0 1 1-.25 11.4 11.4 0 0 0 3.6.57 1 1 0 0 1 1 1V20a1 1 0 0 1-1 1A17 17 0 0 1 3 4a1 1 0 0 1 1-1h3.5a1 1 0 0 1 1 1c0 1.25.2 2.45.57 3.57a1 1 0 0 1-.25 1z"/></svg>
        <span>036-5520-7391</span><span class="contact__gap"></span>
        <svg class="icon" width="17" height="20" viewBox="0 0 24 24"><path d="M12 2a7 7 0 0 0-7 7c0 5 7 13 7 13s7-8 7-13a7 7 0 0 0-7-7zm0 9.5A2.5 2.5 0 1 1 12 6.5a2.5 2.5 0 0 1 0 5z"/></svg>
        <span>Lindenweg 14 · 98560 Tannrode</span>
      </div>
      <div class="contact__line contact__web" style="font-size:38px; margin-top:16px;">www.steinmetz-hollbach.de</div>
    </div>
  </div>
</section>

<section class="view view--left">
  <div class="panel" style="left:50px; top:200px; width:1100px; height:170px;">
    <svg class="panel__art" viewBox="0 0 1100 170" preserveAspectRatio="none" aria-hidden="true">
      <rect width="1100" height="170" fill="#ffffff"/>
      <path d="M1100 0 H420 C360 50 320 110 240 170 H1100 Z" fill="#2f4944"/>
      <path d="M430 14 C380 60 340 120 290 170" fill="none" stroke="#ffffff" stroke-width="5"/>
      <path d="M400 0 C350 50 300 120 200 170" fill="none" stroke="#c6a45c" stroke-width="6"/>
    </svg>
    <div class="wordmark wordmark--gold" style="left:40px; top:68px; font-size:28px;"><span class="wordmark__dot"></span>Hollbach</div>
    <div class="contact" style="left:500px; top:45px;">
      <div class="contact__line" style="font-size:17px;">
        <svg class="icon" width="16" height="16" viewBox="0 0 24 24"><path d="M6.6 10.8a15 15 0 0 0 6.6 6.6l2.2-2.2a1 1 0 0 1 1-.25 11.4 11.4 0 0 0 3.6.57 1 1 0 0 1 1 1V20a1 1 0 0 1-1 1A17 17 0 0 1 3 4a1 1 0 0 1 1-1h3.5a1 1 0 0 1 1 1c0 1.25.2 2.45.57 3.57a1 1 0 0 1-.25 1z"/></svg>
        <span>036-5520-7391</span><span class="contact__gap"></span>
        <svg class="icon" width="14" height="16" viewBox="0 0 24 24"><path d="M12 2a7 7 0 0 0-7 7c0 5 7 13 7 13s7-8 7-13a7 7 0 0 0-7-7zm0 9.5A2.5 2.5 0 1 1 12 6.5a2.5 2.5 0 0 1 0 5z"/></svg>
        <span>Lindenweg 14 · 98560 Tannrode</span>
      </div>
      <div class="contact__line contact__web" style="font-size:32px; margin-top:14px;">www.steinmetz-hollbach.de</div>
    </div>
  </div>
  <div class="door" style="left:435px; top:460px;">
    <div class="wordmark wordmark--light"><span class="wordmark__dot"></span>Hollbach</div>
  </div>
</section>

</body>
</html>
```